New Business and Accounting Software need a Web Site

The website is for a Business and Accounting Software that has 8 products.
Each product has its owns logo and color, when you do the design have in consideration that we are looking the experience that when you change from one product page to another the look and feel adjust to the color and logo of the product.
The product are:
Ventas (Sales)
Compras (Purchases)
Contabilidad (Accounting)
Presupuesto (Budget)
Inventarios (Inventory)
Bancos (Banks)
NĂ³mina RH (Human Resources Payroll)
CRM (Customer Relationship Manager)

You can see how the main logo and variations are used in each page
- https://www.ufta.com/
- https://www.vemi.com/
- https://www.prulvin.com/

Our goal is to be similar to them.

I have created a word document to explain what I want.
You need to design:
1 Home Page
1 Product Landing Page
1 Product Detail Page
1 Price Page

I am attaching:
1. Main Logo
2. 8 Product Logos
3. Website Idea, you can create your own idea.

You are welcome to use other icons for the each product if you want.

Target Market(s)

Independet professionals and Small and Medium Companies

Industry/Entity Type

Business and Accounting Software

Coding

Coded - Design and coding required

Colors
0054AA
0677BA
7BADD7
CADEEF
E8F1F8

Requirements
Must have
• Must show all products in the main page

```html
<!DOCTYPE html>
<html lang="es">
<head>
<meta charset="utf-8">
<title>tallo — Platform to Run Your Business</title>
<link rel="stylesheet" href="https://fonts.googleapis.com/css2?family=Poppins:wght@400;500;600;700;800&display=swap">
<style>
:root{
  --blue:#0054aa;
  --blue-mid:#0677ba;
  --blue-soft:#7badd7;
  --blue-pale:#cadeef;
  --blue-mist:#e8f1f8;
  --green:#22b58f;
  --orange:#f08a2c;
  --purple:#c86fd0;
  --red:#d65a5f;
  --teal:#3bb28c;
  --ink:#2b2b2b;
  --text:#555b66;
  --footer:#232323;
  --white:#fff;
}
*{box-sizing:border-box;margin:0;padding:0}
html,body{width:1200px;height:3484px;overflow:hidden}
body{position:relative;background:var(--white);font-family:'Poppins',sans-serif;color:var(--text)}
.abs{position:absolute}
a{color:inherit;text-decoration:none}

/* hero */
.hero-shape{position:absolute;left:0;top:0}
.brand{position:absolute;display:flex;align-items:center;gap:8px;color:var(--white);font-weight:700;font-size:34px;letter-spacing:-.5px}
.brand .dot{width:46px;height:46px;border-radius:50%;background:var(--white);opacity:.95}
.nav{position:absolute;left:383px;top:50px;display:flex;gap:28px;color:var(--white);font-size:15px;font-weight:500}
.btn{position:absolute;display:flex;align-items:center;justify-content:center;border-radius:30px;font-weight:600;font-size:14px;letter-spacing:.3px}
.btn-outline{border:2px solid var(--blue);color:var(--blue);background:var(--white)}
.btn-blue{background:var(--blue);color:var(--white)}
.btn-white{background:var(--white);color:var(--blue)}
.btn-green{background:var(--green);color:var(--white)}
.hero-title{position:absolute;left:158px;top:146px;color:var(--white);font-weight:800;font-size:47px;line-height:48px}
.ph{position:absolute;border-radius:8px}

/* products */
.product{position:absolute;padding:40px 0 0 42px}
.product h3{display:flex;align-items:center;gap:12px;font-weight:500;font-size:18px;letter-spacing:.5px;margin-left:-42px;padding-left:2px}
.product h3 .mark{width:26px;height:26px;border-radius:50%;border:3px solid currentColor;flex:none}
.product p{font-size:14px;line-height:18px;color:var(--text);width:155px;margin-top:4px}
.product .more{display:inline-block;margin-top:8px;font-size:13px;color:var(--blue);border-bottom:1px solid var(--blue)}
.product .art{position:absolute;right:4px;bottom:36px;width:62px;height:62px;border-radius:10px;opacity:.3}
.product.active{background:var(--purple);padding:44px 0 0 28px}
.product.active h3{margin-left:0;color:var(--white)}
.product.active p{color:var(--white)}
.product.active .more{color:var(--white);border-color:var(--white)}
.divider-v{position:absolute;width:1px;background:#eceef2}
.divider-h{position:absolute;height:1px;background:#eceef2}

/* feature cards */
.card{position:absolute;border-radius:8px;padding:30px 28px;box-shadow:0 6px 24px rgba(0,40,90,.08);background:var(--white)}
.card h4{font-size:20px;font-weight:600;color:var(--ink);margin-bottom:10px}
.card p{font-size:14px;line-height:18px;color:var(--text)}
.card p+p{margin-top:18px}
.card.green{background:var(--green)}
.card.red{background:var(--red)}
.card.green h4,.card.red h4,.card.green p,.card.red p{color:var(--white)}

/* tabs */
.tabs{position:absolute;left:0;top:1795px;width:1200px;height:103px;background:var(--blue)}
.tabs a{position:absolute;top:44px;color:var(--white);font-size:15px;font-weight:500}
.tabs .notch{position:absolute;left:544px;bottom:0;width:0;height:0;border-left:9px solid transparent;border-right:9px solid transparent;border-bottom:9px solid var(--white)}

.detail-title{position:absolute;left:158px;top:1960px;color:var(--green);font-size:38px;font-weight:800;letter-spacing:1px}
.check-list{position:absolute;left:158px;top:2020px;width:390px;list-style:none}
.check-list li{position:relative;padding-left:21px;font-size:14.5px;line-height:21px;margin-bottom:19px}
.check-list svg{position:absolute;left:0;top:4px}

.feature{position:absolute;top:2372px;width:220px;text-align:center}
.feature .ring{width:100px;height:100px;margin:0 auto;border-radius:50%;border:2px solid var(--blue);display:flex;align-items:center;justify-content:center}
.feature .ring.fill{background:var(--blue)}
.feature h5{font-size:22px;font-weight:500;color:var(--ink);margin-top:18px}
.feature p{font-size:14.5px;line-height:21px;margin-top:6px}

/* cta */
.cta{position:absolute;left:0;top:2665px;width:1200px;height:226px;background:var(--blue)}
.cta-title{position:absolute;left:158px;top:2708px;color:var(--white);font-weight:700;font-size:29px;line-height:31px}

/* footer */
.footer{position:absolute;left:0;top:2891px;width:1200px;height:593px;background:var(--footer);color:#cfd2d6}
.fcol{position:absolute;top:178px}
.fcol h6{font-size:16px;font-weight:600;color:var(--white);letter-spacing:.5px;margin-bottom:14px}
.fcol a{display:block;font-size:12.5px;letter-spacing:.6px;line-height:24.5px}
.fcol h6.next{margin-top:24px}
.newsletter{position:absolute;left:783px;top:178px;width:260px}
.newsletter h6{font-size:16px;font-weight:600;color:var(--white);letter-spacing:.5px}
.email-field{margin-top:22px;border-bottom:1px solid #8a8d92;padding-bottom:4px;font-size:12.5px;display:flex;justify-content:space-between;letter-spacing:.5px}
.newsletter p{font-size:11.5px;line-height:17px;margin-top:18px}
.socials{display:flex;gap:13px;margin-top:18px}
.socials span{width:20px;height:20px;border:1.5px solid #cfd2d6;border-radius:50%}
.copyright{position:absolute;left:0;width:1200px;top:555px;text-align:center;font-size:11px;color:#a6a9ad}
</style>
</head>
<body>

<!-- HERO -->
<svg class="hero-shape" width="1200" height="600" viewBox="0 0 1200 600" role="img" aria-label="Photo of a smiling businessman working at a laptop, tinted blue">
  <defs>
    <linearGradient id="heroTint" x1="0" y1="0" x2="1" y2="1">
      <stop offset="0" stop-color="#1b5fae"/>
      <stop offset=".45" stop-color="#0e57ab"/>
      <stop offset="1" stop-color="#0054aa"/>
    </linearGradient>
  </defs>
  <path d="M0 0H752C745 150 640 190 560 300C490 410 430 585 240 588C140 590 50 560 0 535Z" fill="url(#heroTint)"/>
</svg>

<div class="brand" style="left:60px;top:30px"><span class="dot"></span>tallo</div>
<nav class="nav"><a>Inido</a><a>Soluciones</a><a>Planes</a><a>Contacto</a></nav>
<a class="btn btn-outline" style="left:767px;top:38px;width:181px;height:43px">SIGN IN</a>
<a class="btn btn-blue" style="left:958px;top:38px;width:181px;height:43px">FREE TRIAL</a>

<h1 class="hero-title">All-in-One<br>Platform to Run<br>Your Business.</h1>
<a class="btn btn-white" style="left:158px;top:323px;width:183px;height:42px">FREE TRIAL</a>

<div class="ph" role="img" aria-label="Desktop monitor showing the accounting software dashboard" style="left:575px;top:130px;width:467px;height:452px;background:linear-gradient(160deg,#f1f4f8,#d9dee5 70%,#c3c9d1);border-radius:14px"></div>

<!-- PRODUCTS -->
<div class="divider-v" style="left:368px;top:649px;height:393px"></div>
<div class="divider-v" style="left:602px;top:649px;height:393px"></div>
<div class="divider-v" style="left:831px;top:649px;height:393px"></div>
<div class="divider-h" style="left:158px;top:855px;width:884px"></div>

<div class="product" style="left:158px;top:649px;width:210px;height:206px">
  <h3 style="color:var(--orange)"><span class="mark"></span>VENTAS</h3>
  <p>Quis autem vel eu iure reprehe nderitqu in ea volu...</p><a class="more">Learn More</a>
  <div class="art" role="img" aria-label="Handshake and money bag illustration" style="background:var(--orange)"></div>
</div>
<div class="product" style="left:385px;top:649px;width:217px;height:206px">
  <h3 style="color:var(--blue-soft)"><span class="mark"></span>COMPRAS</h3>
  <p>Quis autem vel eu iure reprehe nderitqu in ea volu...</p><a class="more">Learn More</a>
  <div class="art" role="img" aria-label="Hand holding a phone with shopping cart illustration" style="background:var(--blue-soft)"></div>
</div>
<div class="product active" style="left:602px;top:649px;width:229px;height:206px">
  <h3>CONTABILIDAD</h3>
  <p>Quis autem vel eu iure reprehe nderitqu in ea volu...</p><a class="more">Learn More</a>
  <div class="art" role="img" aria-label="Ledger and calculator illustration" style="background:var(--white);opacity:.35;right:0;bottom:0;width:80px;height:80px"></div>
</div>
<div class="product" style="left:850px;top:649px;width:192px;height:206px">
  <h3 style="color:var(--green)"><span class="mark"></span>PRESUPUESTO</h3>
  <p>Quis autem vel eu iure reprehe nderitqu in ea volu...</p><a class="more">Learn More</a>
  <div class="art" role="img" aria-label="Money bag and coins illustration" style="background:var(--green);right:-10px"></div>
</div>

<div class="product" style="left:158px;top:861px;width:210px;height:181px">
  <h3 style="color:var(--red)"><span class="mark"></span>INVENTARIOS</h3>
  <p>Quis autem vel eu iure reprehe nderitqu in ea volu...</p><a class="more">Learn More</a>
  <div class="art" role="img" aria-label="Stacked boxes with clipboard illustration" style="background:var(--red);bottom:4px"></div>
</div>
<div class="product" style="left:385px;top:861px;width:217px;height:181px">
  <h3 style="color:var(--ink)"><span class="mark"></span>BANCOS</h3>
  <p>Quis autem vel eu iure reprehe nderitqu in ea volu...</p><a class="more">Learn More</a>
  <div class="art" role="img" aria-label="Bank building illustration" style="background:var(--ink);bottom:4px"></div>
</div>
<div class="product" style="left:618px;top:861px;width:213px;height:181px">
  <h3 style="color:var(--teal)"><span class="mark"></span>NÓMINA RH</h3>
  <p>Quis autem vel eu iure reprehe nderitqu in ea volu...</p><a class="more">Learn More</a>
  <div class="art" role="img" aria-label="Payroll envelope with banknotes illustration" style="background:var(--teal);bottom:4px"></div>
</div>
<div class="product" style="left:850px;top:861px;width:192px;height:181px">
  <h3 style="color:var(--blue)"><span class="mark"></span>CRM</h3>
  <p>Quis autem vel eu iure reprehe nderitqu in ea volu...</p><a class="more">Learn More</a>
  <div class="art" role="img" aria-label="Customer with charts illustration" style="background:var(--blue);bottom:4px;right:-10px"></div>
</div>

<!-- FEATURE CARDS -->
<div class="ph" role="img" aria-label="Dark photo of hands typing on a laptop with data graphics" style="left:0;top:1147px;width:402px;height:450px;border-radius:0 6px 6px 0;background:linear-gradient(135deg,#3c4a5e,#1f2a3a)"></div>
<div class="ph" role="img" aria-label="Photo of a hand signing documents with a pen" style="left:124px;top:1241px;width:406px;height:450px;background:linear-gradient(140deg,#e8e6e2,#c9c6c0);box-shadow:0 10px 30px rgba(0,0,0,.18)"></div>

<div class="card green" style="left:598px;top:1172px;width:208px;height:236px">
  <h4>Sed ut Perspici</h4>
  <p>Nemo enim ipsam voluptatem quia vo luptas sit aspernatur aut odit aut</p>
  <p>Dugit, sed quia con sequuntur magni do lores eos...</p>
</div>
<div class="card" style="left:836px;top:1131px;width:206px;height:237px">
  <h4>Magnam Aliqu</h4>
  <p>Nemo enim ipsam voluptatem quia vo luptas sit aspernatur aut odit aut</p>
  <p>Dugit, sed quia con sequuntur magni do lores eos...</p>
</div>
<div class="card" style="left:598px;top:1440px;width:208px;height:238px">
  <h4>Sed ut Perspici</h4>
  <p>Nemo enim ipsam voluptatem quia vo luptas sit aspernatur aut odit aut</p>
  <p>Dugit, sed quia con sequuntur magni do lores eos...</p>
</div>
<div class="card red" style="left:836px;top:1399px;width:206px;height:238px">
  <h4>Dolorem eum</h4>
  <p>Nemo enim ipsam voluptatem quia vo luptas sit aspernatur aut odit aut</p>
  <p>Dugit, sed quia con sequuntur magni do lores eos...</p>
</div>

<!-- PRODUCT TABS -->
<nav class="tabs">
  <a style="left:189px">Ventas</a>
  <a style="left:273px">Compras</a>
  <a style="left:376px">Contabilidad</a>
  <a style="left:511px">Presupuesto</a>
  <a style="left:643px">Inventarios</a>
  <a style="left:764px">Bancos</a>
  <a style="left:855px">Nómina RH</a>
  <a style="left:975px">CRM</a>
  <span class="notch"></span>
</nav>

<h2 class="detail-title">PRESUPUESTO</h2>
<ul class="check-list">
  <li><svg width="14" height="14" viewBox="0 0 14 14"><circle cx="7" cy="7" r="6" fill="none" stroke="#22b58f" stroke-width="1.5"/><path d="M4 7.2l2 2 4-4.4" fill="none" stroke="#22b58f" stroke-width="1.6"/></svg>Lorem ipsum dolor sit amet, consectetur adipisc ing elit, sed do eiusmod tempor incididunt ut labore et dolore magna aliqua.</li>
  <li><svg width="14" height="14" viewBox="0 0 14 14"><circle cx="7" cy="7" r="6" fill="none" stroke="#22b58f" stroke-width="1.5"/><path d="M4 7.2l2 2 4-4.4" fill="none" stroke="#22b58f" stroke-width="1.6"/></svg>Ut enim ad minim veniam, quis nostrud exercita tion ullamco laboris nisi ut aliquip ex ea commodo consequat. Duis aute irure</li>
  <li><svg width="14" height="14" viewBox="0 0 14 14"><circle cx="7" cy="7" r="6" fill="none" stroke="#22b58f" stroke-width="1.5"/><path d="M4 7.2l2 2 4-4.4" fill="none" stroke="#22b58f" stroke-width="1.6"/></svg>Dolor in reprehenderit in voluptate velit esse cillum dolore eu fugiat nulla pariatur.</li>
</ul>
<a class="btn btn-green" style="left:158px;top:2256px;width:183px;height:42px">FREE TRIAL</a>

<div class="ph" role="img" aria-label="Laptop showing the budget module screen" style="left:552px;top:1935px;width:544px;height:385px;background:linear-gradient(170deg,#f4f6f9,#dde3ea 75%,#b9c1cb)"></div>

<div class="feature" style="left:127px">
  <div class="ring"><svg width="50" height="50" viewBox="0 0 50 50" fill="none" stroke="#0054aa" stroke-width="2"><rect x="6" y="8" width="38" height="30" rx="2"/><path d="M12 32v-6M19 32v-10M26 32v-8M33 32v-14"/><path d="M12 20l8-5 6 3 10-7"/></svg></div>
  <h5>Enim ad minima</h5><p>Nemo enim ipsam volu quia vo luptas sit aspernatur aut odit aut</p>
</div>
<div class="feature" style="left:366px">
  <div class="ring"><svg width="50" height="50" viewBox="0 0 50 50" fill="none" stroke="#0054aa" stroke-width="2"><circle cx="24" cy="26" r="17"/><circle cx="24" cy="26" r="11"/><circle cx="24" cy="26" r="5"/><path d="M24 26L40 10M36 8l4 2 2 4"/></svg></div>
  <h5>Nisi ut Aliquid</h5><p>Nemo enim ipsam volu quia vo luptas sit aspernatur aut odit aut</p>
</div>
<div class="feature" style="left:614px">
  <div class="ring fill"><svg width="52" height="52" viewBox="0 0 52 52" fill="none" stroke="#fff" stroke-width="2"><rect x="6" y="8" width="40" height="28" rx="2"/><path d="M20 44h12M26 36v8M12 16h10M12 22h10M12 28h6"/><circle cx="35" cy="22" r="6"/></svg></div>
  <h5>Volupas Nulla Ir</h5><p>Nemo enim ipsam volu quia vo luptas sit aspernatur aut odit aut</p>
</div>
<div class="feature" style="left:855px">
  <div class="ring"><svg width="50" height="50" viewBox="0 0 50 50" fill="none" stroke="#0054aa" stroke-width="2"><rect x="8" y="6" width="28" height="38" rx="3"/><rect x="13" y="11" width="18" height="8"/><path d="M14 26h4M22 26h4M14 33h4M22 33h4"/><ellipse cx="38" cy="32" rx="7" ry="3"/><path d="M31 32v8c0 2 14 2 14 0v-8"/></svg></div>
  <h5>Quis autem vel</h5><p>Nemo enim ipsam volu quia vo luptas sit aspernatur aut odit aut</p>
</div>

<!-- CTA -->
<div class="cta"></div>
<svg class="abs" style="left:580px;top:2622px" width="620" height="269" viewBox="0 0 620 269" role="img" aria-label="Photo of a smiling man on the phone holding documents near a window">
  <defs><linearGradient id="ctaPhoto" x1="0" y1="0" x2="1" y2="1"><stop offset="0" stop-color="#5b6f7c"/><stop offset="1" stop-color="#2c3f52"/></linearGradient></defs>
  <path d="M52 43H620V269H0Z" fill="#22b58f"/>
  <path d="M66 43H620V269H14Z" fill="url(#ctaPhoto)"/>
</svg>
<h2 class="cta-title">Neque porro quisqua<br>mest, qui dolorem ipsum<br>qudolor sit a...</h2>
<a class="btn btn-green" style="left:158px;top:2807px;width:183px;height:43px">FREE TRIAL</a>

<!-- FOOTER -->
<footer class="footer">
  <div class="brand" style="left:528px;top:84px;font-size:33px"><span class="dot" style="width:44px;height:44px"></span>tallo</div>
  <div class="fcol" style="left:158px">
    <h6>Community</h6><a>Tutorials</a><a>Documentation</a><a>Forum</a>
    <h6 class="next">Open Source</h6><a>Download</a><a>Codehub</a><a>Testbed</a><a>Translations</a>
  </div>
  <div class="fcol" style="left:367px">
    <h6>Services</h6><a>Ufta.sh Hosting</a><a>Support</a><a>Upgrade</a><a>Education</a><a style="margin-top:10px">Find an Accountant</a><a>Find a Partner</a><a>Become a Partner</a>
  </div>
  <div class="fcol" style="left:589px">
    <h6>About us</h6><a>Our company</a><a>Contact us</a><a>Jobs</a><a>Events</a><a>Blog</a><a>Customers</a><a>Partners</a><a>Legal</a><a>Privacy</a><a>Security</a>
  </div>
  <div class="newsletter">
    <h6>Join Newsletter</h6>
    <div class="email-field"><span>Enter Your Email</span><svg width="14" height="14" viewBox="0 0 14 14"><path d="M1 7L13 1 9 13 7 8Z" fill="#fff"/></svg></div>
    <p>Lorem ipsum dolor sit amet, consectet dipiscing elit, sed do eiusmod tempor incidi dunt ut labore et dolore.</p>
    <div class="socials"><span></span><span></span><span></span><span></span><span></span></div>
  </div>
  <div class="copyright">© Copyright 2022 Accounting Software. All rights reserved.</div>
</footer>

</body>
</html>
```